Website Homepage Design

Daltrove Care Partners Inc. is a Canadian financial services company that specialize in the delivery and administration of alternative health benefit solutions. Daltrove is seeking to adjust their brand and develop a new website.

We like the design and layout of the website below but are not looking for an exact replica (be creative):

http://www.quellaretreat.example/

We want the colour scheme to be clean white and "fresh green", possibly with orange accents (links).

This posting is only for a website homepage design (no coding), but anyone who includes a new logo, in addition to the design, will get priority.

Best of luck,

Oliver
Updates

Project is guaranteed.

Please let me know if you are currently working on a design.

Thank you,

Oliver

*Update:

Two example websites with good colour scheme/design:

- http://budlynest.example/
- http://www.petalkinderhaus.example.au/

I have attached a wireframe and colour scheme to the project brief. The main colour should be the green one. Other colours can be used for highlights and accents, etc.

Target Market(s)

Business owners age 50+

Industry/Entity Type

Financial

Requirements
Must have
• - Clear and simple design
- Area for video (similar to http://www.quellaretreat.example)
Should not have
• - Lots of pictures

```html
<!DOCTYPE html>
<html lang="en">
<head>
<meta charset="utf-8">
<title>Daltrove Care Partners – Home</title>
<link rel="stylesheet" href="https://fonts.googleapis.com/css2?family=Nunito:wght@400;600;800&family=Arimo:ital,wght@0,400;1,400&display=swap">
<style>
  :root {
    --green: #a4c45c;
    --green-dark: #6e9a2c;
    --green-panel: #cfe1a0;
    --orange: #e9951f;
    --orange-light: #f3b23a;
    --blue: #6aa3d4;
    --grey-text: #6d6d6d;
    --body-text: #444;
    --white: #fff;
    --page: #fafafa;
  }
  * { margin: 0; padding: 0; box-sizing: border-box; }
  html, body { width: 1200px; height: 1100px; overflow: hidden; }
  body { background: var(--page); font-family: "Arimo", Arial, sans-serif; position: relative; }

  .site-header { position: absolute; left: 0; top: 0; width: 1200px; height: 128px; }
  .brand { position: absolute; left: 143px; top: 52px; display: flex; align-items: center; gap: 8px;
    font-family: "Nunito", sans-serif; font-weight: 600; font-size: 40px; color: #6b6b6b; letter-spacing: -0.5px; }
  .brand-dot { width: 14px; height: 14px; border-radius: 50%; background: var(--green); }
  .account-tab { position: absolute; left: 894px; top: 0; width: 177px; height: 38px; background: #e8e8e8;
    border-radius: 0 0 8px 8px; display: flex; font-size: 11px; color: #666; }
  .account-tab a { flex: 1; display: flex; align-items: center; justify-content: center; gap: 6px; color: inherit; text-decoration: none; }
  .account-tab a + a { border-left: 1px solid #d2d2d2; }
  .contact-line { position: absolute; right: 136px; top: 78px; display: flex; gap: 28px; font-size: 13px; color: var(--grey-text); }
  .contact-line span { display: flex; align-items: center; gap: 6px; }

  .main-nav { position: absolute; left: 0; top: 128px; width: 1200px; height: 42px; background: linear-gradient(#aacb64, #9cbd53);
    border-bottom: 4px solid var(--orange-light); display: flex; justify-content: center; padding-left: 4px; }
  .main-nav a { color: var(--white); font-family: "Nunito", sans-serif; font-weight: 600; font-size: 14px; text-decoration: none;
    text-shadow: 0 1px 1px rgba(0,0,0,.35); padding: 0 24px; line-height: 38px; border-left: 1px solid rgba(255,255,255,.25); }
  .main-nav a:first-child { border-left: none; }

  .video-frame { position: absolute; left: 110px; top: 185px; width: 960px; height: 464px; background: var(--white);
    box-shadow: 0 0 4px rgba(0,0,0,.25); padding: 10px; }
  .video-screen { position: relative; width: 940px; height: 443px;
    background: radial-gradient(ellipse at 85% 55%, #1c3b4a 0%, rgba(16,30,40,0) 45%), linear-gradient(160deg, #111418, #0a1722 60%, #05080b); }
  .buffer { position: absolute; left: 437px; top: 171px; width: 67px; height: 67px; border-radius: 50%; background: var(--white);
    text-align: center; color: #333; }
  .buffer b { display: block; font-weight: 400; font-size: 19px; padding-top: 16px; }
  .buffer small { display: block; font-size: 7px; letter-spacing: 1px; }
  .play { position: absolute; left: 438px; top: 369px; width: 65px; height: 42px; border-radius: 21px; background: linear-gradient(#fff, #d9d9d9);
    display: flex; align-items: center; justify-content: center; }

  .promo { position: absolute; top: 669px; width: 311px; height: 109px; color: var(--white); text-align: center;
    font-family: "Nunito", sans-serif; text-shadow: 0 1px 2px rgba(0,0,0,.25); display: flex; flex-direction: column; justify-content: center; }
  .promo .kicker { font-size: 23px; font-weight: 400; line-height: 1; }
  .promo .headline { font-size: 28px; font-weight: 800; line-height: 1; margin-top: 4px; }
  .promo-savings { left: 110px; background: linear-gradient(120deg, #f4b93c, #e8901c); border: 1px solid #e98a14; }
  .promo-brochure { left: 435px; background: linear-gradient(120deg, #9cc25a, #6f9e35); border: 1px solid #7da53e; }
  .promo-contact { left: 759px; background: linear-gradient(120deg, #8bbde4, #4d8dc8); border: 1px solid #4c86bd; }

  .site-footer { position: absolute; left: 0; top: 805px; width: 1200px; height: 295px; background: var(--green); }
  .panel { position: absolute; top: 20px; width: 310px; height: 203px; background: var(--green-panel); border: 1px solid #e1edc4; padding: 14px 18px; }
  .panel h2 { font-family: "Nunito", sans-serif; font-weight: 600; font-size: 25px; color: var(--green-dark); margin-bottom: 10px; }
  .panel p { font-size: 13px; line-height: 21px; color: var(--body-text); }
  .panel-about { left: 110px; }
  .panel-testimonials { left: 437px; }
  .panel-follow { left: 759px; }
  .quote { position: relative; font-style: italic; padding-left: 0; }
  .quote .mark { position: absolute; left: 2px; top: -6px; font-family: Georgia, serif; font-size: 58px; color: var(--white); font-style: normal; line-height: 1; }
  .quote .indent { padding-left: 54px; }
  .quote-author { text-align: right; font-size: 14px; color: var(--body-text); margin-top: 2px; }
  .btn { position: absolute; bottom: 17px; right: 20px; width: 146px; height: 34px; border-radius: 8px; background: linear-gradient(var(--orange-light), var(--orange));
    border: 1px solid #fff; color: var(--white); font-family: "Nunito", sans-serif; font-size: 16px; line-height: 32px; padding-left: 23px; text-decoration: none; }
  .social { display: flex; gap: 5px; margin-top: 18px; }
  .social span { width: 64px; height: 64px; border-radius: 4px; display: flex; align-items: center; justify-content: center; }
  .s-one { background: linear-gradient(#7fd8f5, #3bb6e6); }
  .s-two { background: linear-gradient(#5873aa, #374f86); }
  .s-mail { background: linear-gradient(#e02a1f, #b8140c); }
  .s-feed { background: linear-gradient(#fba43a, #ee7d12); }
  .footer-brand { position: absolute; left: 114px; top: 250px; display: flex; align-items: center; gap: 6px;
    font-family: "Nunito", sans-serif; font-weight: 600; font-size: 28px; color: var(--white); }
  .footer-brand i { width: 10px; height: 10px; border-radius: 50%; background: var(--white); }
  .legal { position: absolute; right: 133px; top: 238px; text-align: right; font-size: 11px; color: var(--white); line-height: 23px; }
  .legal a { color: var(--white); text-decoration: none; }
</style>
</head>
<body>
  <header class="site-header">
    <div class="brand"><span>daltrove</span><span class="brand-dot"></span></div>
    <div class="account-tab">
      <a href="#"><svg width="9" height="12" viewBox="0 0 9 12"><rect x="0" y="5" width="9" height="7" fill="#777"/><path d="M2 5V3a2.5 2.5 0 0 1 5 0v2" stroke="#777" stroke-width="1.5" fill="none"/></svg>LOGIN</a>
      <a href="#"><svg width="12" height="12" viewBox="0 0 12 12"><circle cx="6" cy="3.5" r="3" fill="#777"/><path d="M0 12a6 5 0 0 1 12 0z" fill="#777"/></svg>SIGNUP</a>
    </div>
    <div class="contact-line">
      <span><svg width="11" height="18" viewBox="0 0 11 18"><rect x="0.5" y="0.5" width="10" height="17" rx="1.5" fill="none" stroke="#777"/><rect x="2.5" y="3" width="6" height="5" fill="#777"/><rect x="2.5" y="10" width="6" height="5" fill="#999"/></svg>604.555.0192</span>
      <span><svg width="17" height="13" viewBox="0 0 17 13"><path d="M1 5l7.5-4 7.5 4v7H1z" fill="none" stroke="#777" stroke-width="1.5"/><path d="M1 5l7.5 5 7.5-5" fill="none" stroke="#777" stroke-width="1.5"/></svg>info@daltrove.example</span>
    </div>
  </header>

  <nav class="main-nav">
    <a href="#">HOME</a><a href="#">ABOUT DALTROVE</a><a href="#">INCORPORATED</a><a href="#">EXCLUSIVE BENEFITS</a><a href="#">FORMS</a><a href="#">CONTACT US</a>
  </nav>

  <section class="video-frame">
    <div class="video-screen" role="img" aria-label="Introductory video with dark abstract light streaks">
      <div class="buffer"><b>0%</b><small>BUFFERING</small></div>
      <div class="play"><svg width="20" height="22" viewBox="0 0 20 22"><path d="M1 1l18 10L1 21z" fill="#333"/></svg></div>
    </div>
  </section>

  <a class="promo promo-savings" href="#"><span class="kicker">reduce cost</span><span class="headline">CALCULATE<br>YOUR SAVINGS</span></a>
  <a class="promo promo-brochure" href="#"><span class="kicker">how it works</span><span class="headline">VIEW BROCHURE</span></a>
  <a class="promo promo-contact" href="#"><span class="kicker">questions?</span><span class="headline">CONTACT US TODAY</span></a>

  <footer class="site-footer">
    <article class="panel panel-about">
      <h2>ABOUT DALTROVE</h2>
      <p>Daltrove Care Partners Inc. is a Canadian financial services company that specialize in the delivery and administration of alternative health benefit solutions.</p>
      <a class="btn" href="#">Learn more..</a>
    </article>
    <article class="panel panel-testimonials">
      <h2>TESTIMONIALS</h2>
      <p class="quote"><span class="mark">“</span><span class="indent">Sed ut perspiciatis unde omnis iste</span><br><span class="indent">natus error sit voluptatem accusan-</span><br>tium doloremque laudantium, totam rem</p>
      <p class="quote-author">Eaque voluptatem</p>
      <a class="btn" href="#">View more..</a>
    </article>
    <article class="panel panel-follow">
      <h2>FOLLOW DALTROVE</h2>
      <p>Follow us on your favorite social networking</p>
      <div class="social">
        <span class="s-one" role="img" aria-label="Social network link"></span>
        <span class="s-two" role="img" aria-label="Social network link"></span>
        <span class="s-mail" role="img" aria-label="Email"><svg width="40" height="28" viewBox="0 0 40 28"><rect x="1.5" y="1.5" width="37" height="25" fill="#fff"/><path d="M2 2l18 14L38 2M2 26l14-12M38 26L24 14" stroke="#c4170e" stroke-width="3" fill="none"/></svg></span>
        <span class="s-feed" role="img" aria-label="News feed"><svg width="36" height="36" viewBox="0 0 36 36"><circle cx="6" cy="30" r="5" fill="#fff"/><path d="M2 15a19 19 0 0 1 19 19M2 3a31 31 0 0 1 31 31" stroke="#fff" stroke-width="6" fill="none"/></svg></span>
      </div>
    </article>
    <div class="footer-brand"><span>daltrove</span><i></i></div>
    <div class="legal">Copyright ©2001-2011 DALTROVE<br><a href="#">Privacy Notice</a> | <a href="#">Terms of Use</a> | <a href="#">Disclaimer</a></div>
  </footer>
</body>
</html>
```